Pool service company wants new Wix website design

I want a multi-page website including:
Home
About Us
Services Offered
Contact
Products page
Blog
Target Market(s)
Swimming pool owners. Residential only.
Industry/Entity Type
Swimming pool care, service, maintenance and repair.
Other font styles liked:
- Arial, Calibre
Requirements
Must have
- Wix compatible.

```html
<!DOCTYPE html>
<html lang="en">
<head>
<meta charset="utf-8">
<title>Bluecrest Pool &amp; Spa Service</title>
<link rel="stylesheet" href="https://fonts.googleapis.com/css2?family=Roboto:wght@400;500;700;900&display=swap">
<style>
:root{
  --red:#e8401c;
  --blue:#1f5ea8;
  --blue-head:#1d6ab3;
  --ink:#1e1e1e;
  --body:#444;
  --dark:#151515;
  --white:#fff;
}
*{margin:0;padding:0;box-sizing:border-box}
html,body{width:1200px;height:3508px;overflow:hidden;background:var(--white)}
body{position:relative;font-family:'Roboto',Arial,sans-serif;color:var(--ink)}
.abs{position:absolute}
a{color:inherit;text-decoration:none}

/* header */
.brand{position:absolute;left:72px;top:62px;display:flex;align-items:center;gap:12px}
.brand-dot{width:42px;height:42px;border-radius:50%;background:var(--red)}
.brand-name{font-size:40px;font-weight:900;color:var(--blue)}
.top-contact{position:absolute;top:20px;right:72px;display:flex;gap:16px;align-items:center;font-size:18px;color:var(--blue-head)}
.top-contact span{display:flex;align-items:center;gap:10px}
.top-contact .phone{font-weight:700}
.icon-badge{width:36px;height:36px;border-radius:50%;background:var(--blue);display:flex;align-items:center;justify-content:center}
.nav{position:absolute;top:82px;right:72px;display:flex;gap:36px;font-size:17px;font-weight:500;letter-spacing:.3px}
.nav .active{color:var(--red)}

/* hero */
.hero{position:absolute;left:0;top:120px;width:1200px;height:780px}
.hero-text{position:absolute;left:75px;top:194px;color:var(--white)}
.hero-text .welcome{font-size:58px;font-weight:700;letter-spacing:2px;line-height:1}
.hero-text .name{font-size:92px;font-weight:700;letter-spacing:3px;line-height:82px;margin-top:2px}
.hero-text .tag{font-size:36px;font-weight:700;letter-spacing:1px;line-height:40px;margin-top:4px}
.btn{display:inline-flex;align-items:center;justify-content:center;background:var(--red);color:var(--white);font-weight:700;font-size:17px;border-radius:26px;height:49px;width:163px}
.hero .btn{position:absolute;left:75px;top:392px}
.dots{position:absolute;left:75px;top:473px;display:flex;gap:12px}
.dots i{width:9px;height:9px;border-radius:50%;background:#5aa7e8}
.dots i:first-child{background:var(--white)}

/* headings */
.section-title{position:absolute;left:0;width:1200px;text-align:center;font-size:46px;font-weight:700;letter-spacing:1.5px;color:var(--ink)}

/* services */
.service{position:absolute;top:1040px;width:362px;text-align:center}
.service .photo{position:relative;margin:0 auto;width:324px;height:324px;border-radius:50%;border:5px solid var(--white);box-shadow:0 0 0 2px #e4e4e4,0 6px 14px rgba(0,0,0,.12)}
.service .ico{position:absolute;right:-6px;bottom:-6px;width:98px;height:98px;border-radius:50%;background:var(--blue);border:4px solid var(--white);display:flex;align-items:center;justify-content:center}
.card-title{font-size:30px;font-weight:700;color:var(--blue-head);letter-spacing:.5px;line-height:35px}
.service .card-title{margin-top:30px}
.desc{font-size:17px;line-height:25px;color:var(--body);margin-top:10px}
.service .btn,.post .btn{margin-top:20px}

/* about */
.about-band{position:absolute;left:0;top:1636px;width:1200px;height:616px}
.about-photo{position:absolute;left:75px;top:1777px;width:511px;height:398px;border-radius:22px;background:linear-gradient(135deg,#2f8fc4,#66bde0 45%,#2b6c9a)}
.about-text{position:absolute;left:616px;top:1788px;width:510px;color:var(--white)}
.about-text h2{font-size:48px;line-height:47px;font-weight:700;letter-spacing:1.5px}
.about-text p{font-size:17px;line-height:30.5px;margin-top:22px}
.btn-outline{display:inline-flex;align-items:center;justify-content:center;width:177px;height:49px;border:2px solid var(--white);border-radius:26px;font-weight:700;font-size:17px;margin-top:24px}
.mascot{position:absolute}

/* blog */
.post{position:absolute;top:2400px;width:328px;text-align:center}
.post .thumb{position:relative;height:256px;border-radius:24px;overflow:hidden}
.post .date{position:absolute;left:0;bottom:0;height:52px;width:180px;background:var(--red);color:var(--white);font-weight:700;font-size:20px;display:flex;align-items:center;padding-left:24px;letter-spacing:.5px;clip-path:polygon(0 0,160px 0,180px 100%,0 100%)}
.post .card-title{margin-top:18px}
.arrow{position:absolute;top:2618px}

/* footer */
.footer-bg{position:absolute;left:0;top:2955px;width:1200px;height:553px}
.f-brand{position:absolute;left:75px;top:3130px;display:flex;align-items:center;gap:10px}
.f-brand .brand-name{color:var(--white);font-size:36px}
.f-head{font-size:21px;font-weight:700;color:var(--white);letter-spacing:.5px}
.f-col{position:absolute;color:var(--white)}
.f-col ul{list-style:none;margin-top:18px}
.f-col li{font-size:15px;line-height:40px}
.address{position:absolute;left:75px;top:3246px;color:var(--white)}
.address .row{display:flex;gap:16px;font-size:15px;line-height:24px;margin-top:14px}
.address .row svg{flex:none;margin-top:5px}
.social{display:flex;gap:20px;margin-top:22px}
.social i{display:block;width:21px;height:21px;border-radius:3px;background:var(--white)}

.contact-card{position:absolute;z-index:2;left:704px;top:3069px;width:420px;height:397px;background:var(--white);border-radius:22px;padding:26px 15px}
.contact-card h3{font-size:32px;font-weight:500;letter-spacing:1px;color:var(--ink)}
.field{position:absolute;border:1px solid #9a9a9a;border-radius:25px;font-size:14px;color:#333;padding:0 20px;display:flex;align-items:center}
.field.msg{align-items:flex-start;padding-top:16px;border-radius:26px}
.submit{position:absolute;left:15px;top:322px;width:390px;height:48px;border-radius:25px;background:var(--red);color:var(--white);font-weight:700;font-size:17px;display:flex;align-items:center;justify-content:center}

.copy-bar{position:absolute;z-index:3;left:0;top:3459px;width:624px;height:49px;background:var(--blue);border-radius:0 26px 0 0;color:var(--white);font-size:14px;display:flex;align-items:center;padding-left:73px}
</style>
</head>
<body>

<!-- Header -->
<header>
  <div class="brand"><span class="brand-dot"></span><span class="brand-name">Bluecrest</span></div>
  <div class="top-contact">
    <span class="phone"><span class="icon-badge"><svg width="18" height="18" viewBox="0 0 24 24"><path fill="#fff" d="M6.6 10.8a15 15 0 0 0 6.6 6.6l2.2-2.2c.3-.3.7-.4 1-.2 1.1.4 2.3.6 3.6.6.6 0 1 .4 1 1V20c0 .6-.4 1-1 1A17 17 0 0 1 3 4c0-.6.4-1 1-1h3.5c.6 0 1 .4 1 1 0 1.3.2 2.5.6 3.6.1.3 0 .7-.2 1z"/></svg></span>1-800-555-0142</span>
    <span><span class="icon-badge"><svg width="18" height="14" viewBox="0 0 20 14"><rect x="0" y="0" width="20" height="14" rx="2" fill="#fff"/><path d="M1 1l9 7 9-7" stroke="#1f5ea8" stroke-width="2" fill="none"/></svg></span>hello@bluecrestpools.com</span>
  </div>
  <nav class="nav">
    <a class="active">HOME</a><a>ABOUT US</a><a>SERVICES OFFERED</a><a>PRODUCTS</a><a>BLOG</a><a>CONTACT</a>
  </nav>
</header>

<!-- Hero -->
<section class="hero">
  <svg class="abs" style="left:0;top:0" width="1200" height="780" viewBox="0 0 1200 780">
    <defs>
      <linearGradient id="heroPhoto" x1="0" y1="0" x2="0" y2="1">
        <stop offset="0" stop-color="#6b6356"/>
        <stop offset=".55" stop-color="#7d7466"/>
        <stop offset=".72" stop-color="#4f9bd0"/>
        <stop offset="1" stop-color="#3d8cc9"/>
      </linearGradient>
    </defs>
    <path d="M0 0H1200V650Q1200 690 1140 698L0 760Z" fill="#e8401c"/>
    <path d="M0 0H1200V640Q1200 680 1140 690L0 748Z" fill="url(#heroPhoto)" role="img" aria-label="Photo of a pool technician in blue overalls cleaning a pool beside a stone villa"/>
  </svg>
  <div class="hero-text">
    <div class="welcome">Welcome to</div>
    <div class="name">Bluecrest</div>
    <div class="tag">Pool &amp; Spa Service</div>
  </div>
  <a class="btn">Read More</a>
  <div class="dots"><i></i><i></i><i></i><i></i></div>
</section>

<!-- Services -->
<h2 class="section-title" style="top:952px">Services Offered</h2>

<div class="service" style="left:57px">
  <div class="photo" role="img" aria-label="Photo of a worker cleaning an empty blue-tiled pool" style="background:linear-gradient(160deg,#3c8fd6,#1e6bbf 60%,#4da2e3)">
    <span class="ico"><svg width="50" height="40" viewBox="0 0 50 40" fill="none" stroke="#fff" stroke-width="2.5"><path d="M4 26q6-5 12 0t12 0 12 0 8-2"/><path d="M4 34q6-5 12 0t12 0 12 0 8-2"/><path d="M30 24V6a4 4 0 0 1 8 0"/></svg></span>
  </div>
  <div class="card-title">Swimming Pool Care</div>
  <p class="desc">Sed ut perspiciatis unde omnis iste natus<br>error sit voluptatem accusantium.</p>
  <a class="btn">Read More</a>
</div>

<div class="service" style="left:418px">
  <div class="photo" role="img" aria-label="Photo of two men testing water beside a residential pool" style="background:linear-gradient(180deg,#d8d5c9,#8c8f80 50%,#2a8fd8)">
    <span class="ico"><svg width="46" height="42" viewBox="0 0 46 42" fill="none" stroke="#fff" stroke-width="2.5"><path d="M14 28V6a4 4 0 0 1 8 0M30 28V6a4 4 0 0 1 8 0M14 14h16M14 22h16"/><path d="M3 34q6-4 10 0t10 0 10 0 10 0"/></svg></span>
  </div>
  <div class="card-title">Pool Service</div>
  <p class="desc">Sed ut perspiciatis unde omnis iste natus<br>error sit voluptatem accusantium.</p>
  <a class="btn">Read More</a>
</div>

<div class="service" style="left:781px">
  <div class="photo" role="img" aria-label="Photo of a hand repairing pool tiles with a trowel" style="background:linear-gradient(150deg,#2fa8d8,#5cc4e6 50%,#c08a6e)">
    <span class="ico"><svg width="42" height="42" viewBox="0 0 42 42" fill="none" stroke="#fff" stroke-width="2.5"><circle cx="21" cy="21" r="7"/><path d="M21 3v6M21 33v6M3 21h6M33 21h6M8 8l4 4M30 30l4 4M8 34l4-4M30 12l4-4"/></svg></span>
  </div>
  <div class="card-title">Maintenance &amp; Repair</div>
  <p class="desc">Sed ut perspiciatis unde omnis iste natus<br>error sit voluptatem accusantium.</p>
  <a class="btn">Read More</a>
</div>

<!-- About -->
<svg class="about-band" viewBox="0 0 1200 616">
  <defs>
    <linearGradient id="aboutGrad" x1="0" y1="0" x2="1" y2="0">
      <stop offset="0" stop-color="#1b4f8f"/>
      <stop offset=".5" stop-color="#5a3a66"/>
      <stop offset=".8" stop-color="#b8402a"/>
      <stop offset="1" stop-color="#7a1f12"/>
    </linearGradient>
  </defs>
  <path d="M0 110Q0 72 40 68L1200 0V616H0Z" fill="url(#aboutGrad)" role="img" aria-label="Background photo of pool hoses, tinted blue to red"/>
</svg>
<div class="about-photo" role="img" aria-label="Photo of a smiling pool technician holding a hose and skimmer net"></div>
<div class="about-text">
  <h2>About<br>Bluecrest</h2>
  <p>Sed ut perspiciatis unde omnis iste natus error sit voluptatem accusantium doloremque laudantium, totam rem aperiam, eaque ipsa quae ab illo inventore veritatis et quasi architecto beatae vitae dicta sunt explicabo. Nemo enim ipsam voluptatem quia voluptas sit aspernatur aut odit aut fugit sint occaecat cupidatat non proident, sunt in culpa qui officia deserunt .</p>
  <a class="btn-outline">Read More</a>
</div>
<svg class="mascot" style="left:860px;top:2106px" width="320" height="296" viewBox="0 0 320 296" role="img" aria-label="Cartoon pool cleaner mascot giving a thumbs up with a skimmer pole">
  <defs>
    <radialGradient id="mascotA" cx=".5" cy=".5" r=".5">
      <stop offset="0" stop-color="#2f72c2" stop-opacity=".55"/>
      <stop offset=".6" stop-color="#e4612c" stop-opacity=".25"/>
      <stop offset="1" stop-color="#e4612c" stop-opacity="0"/>
    </radialGradient>
  </defs>
  <ellipse cx="160" cy="148" rx="150" ry="140" fill="url(#mascotA)"/>
</svg>

<!-- Blog -->
<h2 class="section-title" style="top:2310px">Blog Posts</h2>

<svg class="arrow" style="left:44px" width="16" height="26" viewBox="0 0 16 26"><path d="M14 2L3 13l11 11" stroke="#333" stroke-width="2" fill="none"/></svg>
<svg class="arrow" style="left:1140px" width="16" height="26" viewBox="0 0 16 26"><path d="M2 2l11 11L2 24" stroke="#333" stroke-width="2" fill="none"/></svg>

<article class="post" style="left:75px">
  <div class="thumb" role="img" aria-label="Photo of a technician working on a pump at the poolside" style="background:linear-gradient(135deg,#3a9ed6,#8a8a86 50%,#b83a2a)"><span class="date">Jan20, 2023</span></div>
  <div class="card-title">Nemo enim ipsam<br>voluptatem</div>
  <p class="desc">Sed ut perspiciatis unde omnis iste natus<br>error sit voluptatem accusantium.</p>
  <a class="btn">Read More</a>
</article>

<article class="post" style="left:437px">
  <div class="thumb" role="img" aria-label="Photo of a worker vacuuming a pool with a cleaning machine" style="background:linear-gradient(160deg,#1e8ad0,#58b6e8 50%,#3a5a7a)"><span class="date">Jan20, 2023</span></div>
  <div class="card-title">Nemo enim ipsam<br>voluptatem</div>
  <p class="desc">Sed ut perspiciatis unde omnis iste natus<br>error sit voluptatem accusantium.</p>
  <a class="btn">Read More</a>
</article>

<article class="post" style="left:799px">
  <div class="thumb" role="img" aria-label="Photo of a pool technician cleaning a pool in front of a stone house" style="background:linear-gradient(180deg,#8d8778,#6f6a5e 55%,#3e95cf)"><span class="date">Jan20, 2023</span></div>
  <div class="card-title">Nemo enim ipsam<br>voluptatem</div>
  <p class="desc">Sed ut perspiciatis unde omnis iste natus<br>error sit voluptatem accusantium.</p>
  <a class="btn">Read More</a>
</article>

<!-- Footer -->
<svg class="footer-bg" viewBox="0 0 1200 553">
  <path d="M60 76L1200 0V12L60 88Z" fill="#1f5ea8"/>
  <path d="M0 140Q0 88 60 84L1200 8V553H0Z" fill="#151515"/>
</svg>
<svg class="mascot" style="left:950px;top:2918px;z-index:1" width="240" height="200" viewBox="0 0 240 200" role="img" aria-label="Cartoon pool cleaner mascot standing behind the contact form">
  <defs>
    <radialGradient id="mascotB" cx=".5" cy=".55" r=".5">
      <stop offset="0" stop-color="#2f72c2" stop-opacity=".6"/>
      <stop offset=".55" stop-color="#e4612c" stop-opacity=".3"/>
      <stop offset="1" stop-color="#e4612c" stop-opacity="0"/>
    </radialGradient>
  </defs>
  <ellipse cx="120" cy="110" rx="115" ry="95" fill="url(#mascotB)"/>
</svg>

<div class="f-brand"><span class="brand-dot"></span><span class="brand-name">Bluecrest</span></div>

<div class="address">
  <div class="f-head">Contact Address</div>
  <div class="row" style="margin-top:20px"><svg width="18" height="14" viewBox="0 0 18 14"><path d="M1 2l5-1 6 2 5-1v11l-5 1-6-2-5 1z" fill="#e8401c"/></svg><span>Nemo enim ipsam voluptatem<br>Quia voluptas sit asper</span></div>
  <div class="row" style="margin-top:22px"><svg width="18" height="14" viewBox="0 0 24 24"><path fill="#e8401c" d="M6.6 10.8a15 15 0 0 0 6.6 6.6l2.2-2.2c.3-.3.7-.4 1-.2 1.1.4 2.3.6 3.6.6.6 0 1 .4 1 1V20c0 .6-.4 1-1 1A17 17 0 0 1 3 4c0-.6.4-1 1-1h3.5c.6 0 1 .4 1 1 0 1.3.2 2.5.6 3.6.1.3 0 .7-.2 1z"/></svg><span>1-800-555-0142</span></div>
  <div class="row" style="margin-top:22px"><svg width="18" height="14" viewBox="0 0 20 14"><rect width="20" height="14" rx="2" fill="#e8401c"/><path d="M1 1l9 7 9-7" stroke="#151515" stroke-width="2" fill="none"/></svg><span>hello@bluecrestpools.com</span></div>
</div>

<div class="f-col" style="left:342px;top:3118px">
  <div class="f-head">Site Map</div>
  <ul><li>Home</li><li>About Us</li><li>Services Offered</li><li>Products</li><li>Blog</li><li>Contact</li></ul>
</div>

<div class="f-col" style="left:511px;top:3118px">
  <div class="f-head">Services</div>
  <ul><li>Swimming Pool Care</li><li>Service</li><li>Maintenance &amp; Repair</li></ul>
  <div class="f-head" style="margin-top:42px">Follow Us</div>
  <div class="social"><i></i><i></i><i></i><i></i></div>
</div>

<form class="contact-card">
  <h3>Contact Us</h3>
  <div class="field" style="left:15px;top:81px;width:194px;height:49px">Name</div>
  <div class="field" style="left:215px;top:81px;width:194px;height:49px">Email</div>
  <div class="field" style="left:15px;top:142px;width:194px;height:49px">Phone No</div>
  <div class="field" style="left:215px;top:142px;width:194px;height:49px">Subject</div>
  <div class="field msg" style="left:13px;top:201px;width:398px;height:109px">Message</div>
  <div class="submit">Submit Now</div>
</form>

<div class="copy-bar">Copyright © 2023. Bluecrest Pool Care &nbsp;All Rights Reserved</div>

</body>
</html>
```